High-end residential home builder needs a business card design

We need a new business card design for a small residential construction company based in Boise, Idaho. We specialize in building custom high-end homes and remodels, with a focus on great design and craftsmanship.

We would like to use our current logo, but open to new color suggestions.
Just looking for a clean, sharp, modern design that looks high-end.

Target Market(s)

Upscale clientele

Industry/Entity Type

Contractor

Contact Information for Business Card

Company: Stonehaven Custom Builders
Name: Colin Marsh
Phone number: 208 637 4120
Email: ColinMarshSCB@quillpost.net
Website: Stonehavencustombuilders.com

Font styles to use
Serif
Sans Serif

Requirements
Must have
• Company Logo
Company name
My name
My phone number
My email
Company website
Nice to have
• I have attached a few photos of cards that I really like.

```html
<!DOCTYPE html>
<html lang="en">
<head>
<meta charset="utf-8">
<title>Stonehaven Custom Builders – Business Card</title>
<link rel="stylesheet" href="https://fonts.googleapis.com/css2?family=Montserrat:wght@400;500&family=Lato:wght@400&display=swap">
<style>
  :root {
    --bg: #a9adad;
    --paper: #f7f7f5;
    --ink: #2a2a2a;
    --text: #4a4a4a;
    --orange: #e0891f;
    --black-card: #2b2b2d;
    --deboss: #3d3d40;
  }
  * { box-sizing: border-box; margin: 0; padding: 0; }
  html, body {
    width: 1200px; height: 880px; overflow: hidden;
    background: var(--bg);
  }
  .stage {
    width: 1200px; height: 880px;
    display: flex; align-items: center; justify-content: center; gap: 80px;
  }

  /* Front card (portrait, content runs bottom-to-top) */
  .card-front {
    position: relative;
    width: 320px; height: 560px;
    background: var(--paper);
    border: 3px solid var(--orange);
    overflow: hidden;
  }
  .card-front__content {
    position: absolute;
    width: 560px; height: 320px;
    left: -120px; top: 120px;
    transform: rotate(-90deg);
    display: flex; align-items: center; justify-content: space-between;
    padding: 0 44px 0 60px;
  }
  .contact-block {
    display: flex; flex-direction: column; align-items: flex-end;
    text-align: right;
  }
  .person-name {
    font-family: "Montserrat", sans-serif;
    font-weight: 400;
    font-size: 24px;
    letter-spacing: 0.5px;
    color: var(--orange);
    text-transform: uppercase;
    margin-bottom: 22px;
  }
  .icon-row {
    display: flex; gap: 7px; margin-bottom: 14px;
  }
  .icon-row svg { width: 24px; height: 24px; display: block; }
  .contact-line {
    font-family: "Lato", sans-serif;
    font-size: 16.5px;
    color: var(--text);
    line-height: 1.3;
  }
  .brand-front {
    display: flex; flex-direction: column; align-items: center; gap: 10px;
  }
  .brand-front__square {
    width: 22px; height: 22px; background: var(--ink);
  }
  .brand-front__name {
    font-family: "Montserrat", sans-serif;
    font-weight: 500;
    font-size: 15px;
    letter-spacing: 3px;
    color: var(--ink);
    text-transform: uppercase;
  }

  /* Back card (landscape, black with debossed wordmark) */
  .card-back {
    width: 560px; height: 320px;
    background: var(--black-card);
    border-bottom: 6px solid var(--orange);
    display: flex; align-items: center; justify-content: center; gap: 22px;
  }
  .brand-back__square {
    width: 34px; height: 34px; background: var(--deboss);
  }
  .brand-back__name {
    font-family: "Montserrat", sans-serif;
    font-weight: 500;
    font-size: 22px;
    letter-spacing: 4px;
    color: var(--deboss);
    text-transform: uppercase;
    line-height: 1.35;
  }
</style>
</head>
<body>
<main class="stage">

  <section class="card-front" aria-label="Business card front">
    <div class="card-front__content">
      <div class="contact-block">
        <h1 class="person-name">Colin Marsh</h1>
        <div class="icon-row">
          <svg viewBox="0 0 24 24" aria-label="Phone">
            <circle cx="12" cy="12" r="12" fill="var(--orange)"/>
            <path d="M8.5 6.5l2 2-1.2 1.5a7 7 0 0 0 4.7 4.7l1.5-1.2 2 2-1.5 1.8C11.5 17 7 12.5 6.7 8z" fill="#fff"/>
          </svg>
          <svg viewBox="0 0 24 24" aria-label="Email">
            <circle cx="12" cy="12" r="12" fill="var(--orange)"/>
            <rect x="6" y="8" width="12" height="8.5" fill="#fff"/>
            <path d="M6 8l6 4.8L18 8" fill="none" stroke="var(--orange)" stroke-width="1.3"/>
          </svg>
          <svg viewBox="0 0 24 24" aria-label="Website">
            <circle cx="12" cy="12" r="12" fill="var(--orange)"/>
            <circle cx="12" cy="12" r="6" fill="none" stroke="#fff" stroke-width="1.4"/>
            <ellipse cx="12" cy="12" rx="2.6" ry="6" fill="none" stroke="#fff" stroke-width="1.2"/>
            <line x1="6" y1="12" x2="18" y2="12" stroke="#fff" stroke-width="1.2"/>
          </svg>
        </div>
        <p class="contact-line">208 637 4120</p>
        <p class="contact-line">ColinMarshSCB@quillpost.net</p>
        <p class="contact-line">Stonehavencustombuilders.com</p>
      </div>
      <div class="brand-front">
        <span class="brand-front__square"></span>
        <span class="brand-front__name">Stonehaven</span>
      </div>
    </div>
  </section>

  <section class="card-back" aria-label="Business card back">
    <span class="brand-back__square"></span>
    <p class="brand-back__name">Stonehaven<br>Custom Builders</p>
  </section>

</main>
</body>
</html>
```